Home page web design for "Tales from Thee"

We need a home page web design for a start up company that will write memoirs for seniors.
The completed project will need to include PSD files...NO HTML or CSS necessary.
Attached is a brief outline concept that may give you some ideas...but you are the creative professionals, so please feel free to add your ideas. We will also attach some files that show you our logo, brochures, and photos that could be used to give you ideas of our focus.
There will need to be access to the other pages on the home page to include: 'About Us'; 'How We Can Help'; 'Community Sessions'; 'Senior Consulting ' and 'Contact Us'.
Updates

Target Market(s)

Seniors and Baby Boomers

Industry/Entity Type

It Company

Number of Pages Required

1 page

Colors
f9ba93
fbca95
faa54b
faf289
f37123

Requirements
Must have
• Script easy on senior eyes.
• Initial contact number would be 844-4LANTERN
Nice to have
• While the color pallet is non-specific we prefer the warm colors.
• salmon, peach.......
• NOT so much the orange of Halloween:)
• However, please utilize your creativity and put in colors you feel will draw best with your design.

```html
<!DOCTYPE html>
<html lang="en">
<head>
<meta charset="utf-8">
<title>Tales from Thee – Home</title>
<link rel="stylesheet" href="https://fonts.googleapis.com/css2?family=Arimo:ital,wght@1,700&family=Lato:ital,wght@0,400;0,700;1,400&family=Open+Sans:wght@600;700&family=Roboto+Condensed:wght@700&display=swap">
<style>
:root{
  --peach:#f9c996;
  --peach-light:#fbd3a6;
  --orange:#f37123;
  --brown:#8b3a1c;
  --ink:#111;
  --nav-ink:#222;
  --rule:#c9a98a;
  --white:#fff;
}
*{margin:0;padding:0;box-sizing:border-box}
html,body{width:1200px;height:870px;overflow:hidden}
body{position:relative;background:var(--peach);font-family:"Lato",sans-serif;color:var(--ink)}
.page{position:absolute;inset:0;background:linear-gradient(135deg,var(--peach-light),var(--peach) 60%,#f6c08c)}
.hero-photo{position:absolute;left:0;top:0;width:545px;height:870px;
  clip-path:polygon(0 0,492px 0,540px 870px,0 870px);
  background:linear-gradient(160deg,#f2ece6 0%,#d8c4b4 30%,#a88e7e 55%,#6d5a52 80%,#8a4a3a 100%)}
.moment{position:absolute;width:194px;height:194px;border-radius:50%;border:5px solid var(--white);top:650px}
.moment--beach{left:100px;background:linear-gradient(180deg,#f2a45a 0%,#e07a3a 45%,#6b4a3a 70%,#3a2a24 100%)}
.moment--reading{left:317px;background:linear-gradient(160deg,#f4f2f0 0%,#c9d6e4 45%,#5e7fa6 75%,#3b4f6e 100%)}
.navbar{position:absolute;left:325px;top:51px;width:875px;height:61px;background:linear-gradient(180deg,#fff 0%,#f2f2f2 60%,#e6e6e6 100%);
  display:flex;align-items:center;padding-left:32px;gap:0}
.navbar a{font-family:"Open Sans",sans-serif;font-weight:600;font-size:16px;color:var(--nav-ink);text-decoration:none;margin-right:21px;letter-spacing:.1px}
.navbar a.is-active{color:var(--brown)}
.brand{position:absolute;left:80px;top:22px;width:260px;height:120px;display:flex;align-items:center;justify-content:center;gap:10px}
.brand__dot{width:14px;height:14px;border-radius:50%;background:var(--brown)}
.brand__name{font-family:"Lato",sans-serif;font-weight:700;font-size:26px;color:var(--brown)}
.callout{position:absolute;right:34px;top:11px;display:flex;align-items:center;gap:6px}
.callout svg{width:22px;height:22px}
.callout__label{font-family:"Open Sans",sans-serif;font-weight:700;font-size:10px;color:#333;line-height:1}
.callout__number{font-family:"Open Sans",sans-serif;font-weight:700;font-size:16px;color:#5a2f1a;line-height:1.2}
.flourish{position:absolute;width:96px;height:86px;background:#b97a52;opacity:.35}
.flourish--top{left:514px;top:132px}
.flourish--bottom{left:1078px;top:713px}
.story{position:absolute;left:563px;top:192px;width:607px}
.story h1{font-family:"Arimo",sans-serif;font-style:italic;font-weight:700;font-size:35px;line-height:40px;color:var(--ink)}
.story h2{font-family:"Lato",sans-serif;font-style:italic;font-weight:400;font-size:22px;margin-top:12px;color:var(--ink)}
.story p{font-size:14.6px;line-height:18.2px;letter-spacing:.35px;margin-top:14px}
.story p.gap{margin-top:18px}
.actions{position:absolute;left:564px;top:737px;display:flex;gap:23px}
.btn{width:162px;height:44px;border-radius:22px;background:var(--orange);border:2px solid var(--white);
  font-family:"Roboto Condensed",sans-serif;font-weight:700;font-size:17px;color:#1a0d05;display:flex;align-items:center;justify-content:center;text-decoration:none}
.footer-rule{position:absolute;left:558px;top:817px;width:618px;border-top:1px solid var(--rule)}
.copyright{position:absolute;right:32px;top:832px;font-size:14px;letter-spacing:.3px;color:#222}
</style>
</head>
<body>
<div class="page">
  <div class="hero-photo" role="img" aria-label="Photo of a grandfather reading a book with his smiling granddaughter"></div>
  <div class="moment moment--beach" role="img" aria-label="Photo of an elderly couple walking on a beach at sunset"></div>
  <div class="moment moment--reading" role="img" aria-label="Photo of a grandfather reading to a baby"></div>

  <div class="navbar">
    <a href="#" class="is-active">HOME</a>
    <a href="#">ABOUT US</a>
    <a href="#">HOW WE CAN HELP</a>
    <a href="#">COMMUNITY SERVICES</a>
    <a href="#">COMMUNITY SERVICES</a>
    <a href="#">CONTACT US</a>
  </div>

  <div class="brand"><span class="brand__dot"></span><span class="brand__name">Tales from Thee</span></div>

  <div class="callout">
    <svg viewBox="0 0 24 24"><path fill="#8b4a26" d="M6.6 10.8a15.5 15.5 0 0 0 6.6 6.6l2.2-2.2c.3-.3.7-.4 1-.2 1.1.4 2.3.6 3.6.6.6 0 1 .4 1 1V20c0 .6-.4 1-1 1A17 17 0 0 1 3 4c0-.6.4-1 1-1h3.5c.6 0 1 .4 1 1 0 1.3.2 2.5.6 3.6.1.3 0 .7-.2 1z"/></svg>
    <div><div class="callout__label">CALL US NOW!</div><div class="callout__number">844-4LANTERN</div></div>
  </div>

  <div class="flourish flourish--top" role="img" aria-label="Decorative corner ornament"></div>
  <div class="flourish flourish--bottom" role="img" aria-label="Decorative corner ornament"></div>

  <main class="story">
    <h1>Ordinary Lives……<br>Extraordinary Legacies</h1>
    <h2>When a genealogy doesn’t say enough!</h2>
    <p>If you were alive in 100 years, what would you share with your descendants? Now you have a vehicle to help you immortalize your thoughts for the future...specifically for those who will want to know!</p>
    <p>We are not all presidents of countries or CEO’s of fortune 500 companies! But “every life legacy is a gift to be treasured by the next generation.”</p>
    <p class="gap">Does your family host generations of soldiers, doctors, farmers, scientists, mechanics, entrepreneurs, writers, politicians, contractors, pastors, artisans, athletes, musicians, etc..? Generational patterns can often emerge when writing your story that will interest the next generation.</p>
    <p class="gap">A genealogy, while very relevant, doesn’t offer the personal story of the names we find. A biography can place a deeper relevance on the face for future descendants. Every life is a legacy to pass forward and we at Tales from Thee believe everyone should chronicle their life journey in writing. This commitment allows you to be remembered for who you truly are as a person.</p>
    <p class="gap">Think about it....<br>Do you know the triumphs and tribulations of your ancestors?<br>Do you wish you did?<br>Well, so will those falling into your personal family tree.</p>
  </main>

  <div class="actions">
    <a href="#" class="btn">GREAT GIFT IDEA</a>
    <a href="#" class="btn">LEARN MORE</a>
  </div>

  <div class="footer-rule"></div>
  <div class="copyright">Copyright 2014, <strong>Tales from Thee</strong>. All Rights Reserved</div>
</div>
</body>
</html>
```